Website design for Harbourline Bag printing specialist

We need an overhaul of our website front end design. We need a new look and a modern take on the products we sell and service we offer. We sell plain stock in a variety of bag types and offer a printing service of customers branding and logos. Customers request online quotes and this facility must be an easy one step process for users. Our logo is currently green and orange and we are not really looking for re branding at this stage. The final design must communicate that we are the leading printing specialist throughout the country, have been in operation for 15 years and have a vast amount of experience and expertise. The design must instantly show the products available and the ability to request a quote for the desired product.

Target Market(s)

Trade shows, retailers, dentists, food suppliers. wine makers etc etc and anyone that uses carry bags

Industry/Entity Type

Screen Printing

Number of Pages Required

5+ page

Font styles to use
Serif
Sans Serif

Colors

Designer to choose colors to be used in the design.

Requirements
Must have
• Our home page featuring all the products as selectable entities and a short description of what each bag type is when the user hovers over the image.
• Then the product landing pages must show different sizes of that product type. On each page there must be a quick quote button that goes to the quote screen with the features and information to select or include for a quote to be processed. The logo is green and orange and still should have this present but happy to move away from this on the website pages in general.I have so many product pictures and unable to upload them all here. The categories for products are as follows:
• Kraft Paper Bags
• Laminated bags
• Non-woven bags
• Calico bags
• Wine bags
• Florist bags
• Plastic Bags
• Printed Bags
• Gift Boxes
• Tissue paper
• Wrapping Paper
• Custom Bags and Boxes
• There also needs to be a gallery page that showcases work we have done. The ability to have a description for each photo in the gallery would be great.
• A general bag size page would be great and one content page that is about us and another for contact us.
• A free sample button so a user can request a sample. Phone number must be included on this page and unable to submit with a valid phone number.
• Our phone number should be prominent.
• A search feature please.
Nice to have
• Fonts should be in keeping with the design of the website
Should not have
• I dont want users having to scroll too far down to find information. The icons of the bags on the home screen should almost appear on one screen.
• I can upload all my content and pictures so no need to get them from me. I really want your look and feel and design layout that i can then work from.

```html
<!DOCTYPE html>
<html lang="en">
<head>
<meta charset="utf-8">
<title>Harbourline Bag – Paper Bags &amp; Packaging</title>
<link href="https://fonts.googleapis.com/css2?family=Open+Sans:wght@300;400;600;700;800&display=swap" rel="stylesheet">
<style>
:root{
  --green:#7dc242;
  --green-dark:#5fa52b;
  --orange:#f7861f;
  --ink:#222222;
  --text:#444444;
  --muted:#777777;
  --line:#dddddd;
  --soft:#efefef;
  --white:#ffffff;
  --footer:#1e1e1e;
}
*{box-sizing:border-box;margin:0;padding:0}
html,body{width:1200px;height:4276px;overflow:hidden}
body{font-family:"Open Sans",Arial,sans-serif;color:var(--text);background:var(--white);font-size:14px}
ul{list-style:none}
.wrap{width:876px;margin:0 auto;position:relative}
.accent{color:var(--green)}
.btn{display:inline-block;background:var(--green);color:var(--white);font-weight:700;text-transform:uppercase;border:0}

/* top bar */
.topbar{height:48px;background:var(--green);color:var(--white)}
.topbar .wrap{height:48px;display:flex;align-items:center}
.social{display:flex;gap:8px}
.social span{width:28px;height:28px;border-radius:50%;border:2px solid var(--white);display:block}
.topbar .util{margin-left:auto;display:flex;gap:40px;font-size:13px;font-weight:600;align-items:center}
.topbar .util span{display:flex;align-items:center;gap:8px}
.topbar .dot{width:26px;height:26px;border-radius:50%;background:var(--white);display:inline-block}

/* nav */
.nav{height:78px;background:var(--white);box-shadow:0 2px 4px rgba(0,0,0,.08);position:relative;z-index:2}
.nav .wrap{height:78px;display:flex;align-items:center}
.brand{font-size:22px;font-weight:700;color:var(--green-dark);display:flex;align-items:center;gap:8px;width:200px}
.brand i{width:14px;height:14px;background:var(--orange);display:block}
.menu{display:flex;gap:8px;font-size:14px;font-weight:600;color:var(--ink)}
.menu li{padding:6px 14px;border-radius:14px}
.menu li.on{background:var(--green);color:var(--white)}
.search{margin-left:auto;width:208px;height:30px;background:var(--soft);border-radius:15px;font-size:12px;color:var(--muted);display:flex;align-items:center;padding:0 14px;justify-content:space-between}

/* hero */
.hero{height:604px;position:relative;background:linear-gradient(90deg,#2a2a2a 0%,#3a3a3a 55%,#555049 100%)}
.hero .photo{position:absolute;left:430px;top:0;width:770px;height:604px;background:radial-gradient(ellipse at 55% 50%,#8d2a26 0%,#5a3b33 35%,rgba(60,55,50,0) 70%)}
.hero h1{position:absolute;left:125px;top:305px;color:var(--white);font-size:50px;line-height:62px;font-weight:800;letter-spacing:.5px}
.hero .btn{position:absolute;left:125px;top:450px;width:134px;height:48px;line-height:48px;text-align:center;font-size:15px;border-radius:3px}

/* intro */
.intro{height:182px;padding-top:44px;text-align:center}
.intro p{width:870px;margin:0 auto;font-size:17px;font-weight:600;line-height:26px;color:var(--text)}
.intro hr{width:780px;margin:28px auto 0;border:0;border-top:2px dashed #c8c8c8}

/* categories */
.shop{height:720px;padding-top:60px}
.shop-head{display:flex;align-items:center;margin-bottom:40px}
.section-title{font-size:40px;font-weight:400;color:var(--ink)}
.shop-head .sub{margin-left:220px;font-size:40px;color:var(--ink)}
.arrows{margin-left:auto;display:flex;gap:6px}
.arrows span{width:32px;height:32px;border:2px solid var(--ink);display:flex;align-items:center;justify-content:center}
.shop-body{display:flex;gap:32px}
.cat-list li{width:262px;height:37px;background:var(--orange);color:var(--white);font-size:13px;font-weight:700;line-height:37px;padding-left:28px;margin-bottom:9px}
.grid{display:grid;grid-template-columns:repeat(3,176px);column-gap:26px;row-gap:26px;margin-top:10px}
.card{height:214px;border:1px solid var(--line);position:relative;background:var(--white)}
.card .img{height:168px;margin:8px;background:linear-gradient(#f6f6f6,#e9e9e9)}
.card .img.dark{background:#3a3a3a}
.card .tags{position:absolute;right:6px;top:6px;display:flex;flex-direction:column;gap:3px}
.card .tags i{width:22px;height:20px;background:var(--green);display:block}
.card .meta{position:absolute;left:0;right:0;bottom:0;height:36px;border-top:1px solid var(--line);display:flex;align-items:center;justify-content:space-between;padding:0 10px;font-size:12px;color:var(--ink)}
.card .meta b{font-size:20px}
.card .meta small{font-size:10px;margin-right:4px}

/* sample band */
.sample{height:114px;background:var(--green)}
.sample .wrap{height:114px;display:flex;align-items:center;justify-content:space-between}
.sample h2{color:var(--white);font-size:25px;font-weight:700}
.sample .dark{background:#111;color:var(--white);font-size:13px;font-weight:700;padding:12px 28px;border-radius:2px}

/* gallery */
.gallery{height:590px;padding-top:60px}
.gallery .head{display:flex;align-items:center;justify-content:center;margin-bottom:56px}
.gallery .head .arrows{position:absolute;right:162px}
.tiles{display:flex;height:300px;border-top:1px solid var(--line);border-bottom:1px solid var(--line)}
.tiles div{flex:1;position:relative}
.t1{background:linear-gradient(135deg,#ffffff,#cfe0f5 60%,#2f7fd0)}
.t2{background:#2e2e2e;display:flex;align-items:center;justify-content:center;gap:14px}
.t2 span{width:34px;height:34px;border-radius:50%;border:2px solid var(--white);display:block}
.t3{background:linear-gradient(135deg,#8a1a25,#c0392b 50%,#e7b6a1)}
.t4{background:linear-gradient(135deg,#f7f7f7,#bfe3ee 55%,#6ec1dc)}

/* featured */
.featured{height:622px;background:var(--soft);padding-top:70px}
.featured .section-title{text-align:center;margin-bottom:42px}
.feat-row{display:flex;gap:18px}
.feat{width:280px;height:276px;background:var(--white);box-shadow:0 1px 3px rgba(0,0,0,.12)}
.feat .img{height:150px}
.feat .body{padding:10px 14px}
.feat h3{font-size:14px;font-weight:700;color:var(--ink)}
.feat p{font-size:10px;line-height:14px;color:var(--muted);margin-top:4px}
.feat .buy{display:flex;align-items:center;margin-top:14px;gap:6px}
.feat .buy b{font-size:20px;color:var(--ink);margin-right:auto}
.feat .buy small{font-size:10px;margin-right:4px}
.feat .buy .btn{font-size:10px;padding:5px 10px;color:var(--ink)}

/* newsletter */
.newsletter{height:114px;background:var(--green)}
.newsletter .wrap{height:114px;display:flex;align-items:center}
.newsletter h2{color:var(--white);font-size:48px;font-weight:400;width:350px}
.newsletter .field{width:314px;height:34px;background:var(--white);font-size:12px;color:var(--muted);padding:8px 10px}
.newsletter .go{width:84px;height:34px;background:#111;color:var(--white);font-size:13px;font-weight:700;text-align:center;line-height:34px}

/* blog */
.blog{height:584px;background:var(--soft);padding-top:70px}
.blog .section-title{text-align:center;margin-bottom:34px}
.posts{display:flex;gap:20px}
.post{width:279px;height:372px;background:var(--white);box-shadow:0 1px 3px rgba(0,0,0,.15);border-radius:4px;overflow:hidden}
.post .img{height:186px}
.post .body{padding:12px 14px}
.post time{font-size:10px;color:var(--muted);display:flex;align-items:center;gap:6px}
.post time i{width:11px;height:11px;border:1.5px solid var(--green);display:block}
.post h3{font-size:14px;font-weight:700;color:var(--ink);margin-top:14px}
.post p{font-size:11px;line-height:16px;color:var(--muted);margin-top:8px}
.post .btn{font-size:10px;padding:6px 10px;margin-top:16px}

/* about + contact */
.info{height:470px;padding-top:50px}
.info .wrap{display:flex;gap:80px}
.about{width:396px}
.about .section-title,.contact .section-title{font-size:46px}
.about h4{color:var(--green);font-size:14px;font-weight:700;margin-top:36px}
.about p{font-size:11px;line-height:18px;color:var(--muted);margin-top:10px}
.about .more{font-size:11px;font-weight:700;color:var(--green);text-decoration:underline;margin-top:16px;display:block}
.contact{width:400px}
.contact .lead{font-size:11px;color:var(--ink);margin-top:6px}
.form{margin-top:34px;display:flex;flex-wrap:wrap;gap:10px}
.form div{background:#e6e6e6;height:38px;font-size:10px;color:var(--muted);padding:11px 10px}
.form .half{width:185px}
.form .full{width:380px}
.form .msg{height:116px}
.form .btn{font-size:13px;padding:10px 14px;margin-top:10px}

/* footer */
.footer{height:342px;background:var(--footer);color:#ccc;padding-top:66px}
.footer .wrap{display:flex}
.footer .col{width:226px}
.footer h5{color:var(--green);font-size:12px;font-weight:700;margin-bottom:24px}
.footer li{font-size:11px;margin-bottom:19px;display:flex;align-items:center;gap:10px}
.footer li.b::before{content:"";width:4px;height:4px;background:#ccc;border-radius:50%}
.footer .ico{width:26px;height:26px;border-radius:50%;background:var(--white);flex:none}
.copy{height:44px;background:#111;color:#bbb;font-size:11px;text-align:center;line-height:44px}
.copy b{color:var(--white)}
</style>
</head>
<body>

<header>
  <div class="topbar">
    <div class="wrap">
      <div class="social"><span></span><span></span><span></span><span></span><span></span></div>
      <div class="util">
        <span><i class="dot"></i>+1-555-014-2290</span>
        <span><i class="dot"></i>Login</span>
        <span><i class="dot"></i>Cart</span>
      </div>
    </div>
  </div>
  <nav class="nav">
    <div class="wrap">
      <div class="brand"><i></i>Harbourline Bag</div>
      <ul class="menu">
        <li class="on">Home</li><li>Shop</li><li>Gallery</li><li>About us</li><li>Contact us</li>
      </ul>
      <div class="search">Search
        <svg width="14" height="14" viewBox="0 0 14 14"><circle cx="6" cy="6" r="4.5" fill="none" stroke="#333" stroke-width="1.6"/><line x1="9.5" y1="9.5" x2="13" y2="13" stroke="#333" stroke-width="1.6"/></svg>
      </div>
    </div>
  </nav>
</header>

<section class="hero">
  <div class="photo" role="img" aria-label="Smiling shopper in a red dress holding orange paper shopping bags"></div>
  <h1>STOP POLYTHENE....<br>USE PAPER BAGS!!</h1>
  <span class="btn">Buy Now</span>
</section>

<section class="intro">
  <p>Paper Bags &amp; Packaging Have Become The Need Of The Hour For Environmental Reasons &amp; Paper Bags Have Become Something Of A Fashion And Status Symbol</p>
  <hr>
</section>

<section class="shop">
  <div class="wrap">
    <div class="shop-head">
      <h2 class="section-title">Our <span class="accent">Categories</span></h2>
      <h2 class="sub">Shops<span style="color:var(--orange)">»</span><span class="accent">Bags</span></h2>
      <div class="arrows">
        <span><svg width="10" height="12" viewBox="0 0 10 12"><path d="M8 1 2 6l6 5" fill="none" stroke="#222" stroke-width="2"/></svg></span>
        <span><svg width="10" height="12" viewBox="0 0 10 12"><path d="M2 1l6 5-6 5" fill="none" stroke="#222" stroke-width="2"/></svg></span>
      </div>
    </div>
    <div class="shop-body">
      <ul class="cat-list">
        <li>Kraft Paper Bags »</li><li>Laminated bags »</li><li>Non-woven bags »</li><li>Calico bags »</li>
        <li>Wine bags »</li><li>Florist bags »</li><li>Plastic Bags »</li><li>Printed Bags »</li>
        <li>Gift Boxes »</li><li>Tissue Paper »</li><li>Wrapping Paper »</li>
      </ul>
      <div class="grid">
        <div class="card"><div class="img" role="img" aria-label="Yellow kraft paper bag"></div><div class="tags"><i></i><i></i></div><div class="meta">Kraft Paper Bags<span><small>£</small><b>5</b></span></div></div>
        <div class="card"><div class="img dark" role="img" aria-label="Dark printed gift bag"></div><div class="tags"><i></i><i></i></div><div class="meta">Printed Bags<span><small>£</small><b>6</b></span></div></div>
        <div class="card"><div class="img" role="img" aria-label="Natural non-woven tote bag"></div><div class="tags"><i></i><i></i></div><div class="meta">Non-woven bags<span><small>£</small><b>4</b></span></div></div>
        <div class="card"><div class="img" role="img" aria-label="Brown bottle wine bag"></div><div class="tags"><i></i><i></i></div><div class="meta">Wine bags<span><small>£</small><b>9</b></span></div></div>
        <div class="card"><div class="img" role="img" aria-label="Black plastic carry bag"></div><div class="tags"><i></i><i></i></div><div class="meta">Plastic Bags<span><small>£</small><b>2</b></span></div></div>
        <div class="card"><div class="img" role="img" aria-label="White laminated carrier box"></div><div class="tags"><i></i><i></i></div><div class="meta">Laminated bags<span><small>£</small><b>8</b></span></div></div>
      </div>
    </div>
  </div>
</section>

<section class="sample">
  <div class="wrap">
    <h2>GET FREE SAMPLE TODAY OF OUR PRODUCTS</h2>
    <span class="dark">REQUEST NOW</span>
  </div>
</section>

<section class="gallery">
  <div class="wrap">
    <div class="head">
      <h2 class="section-title">View Our <span class="accent">Gallery</span></h2>
    </div>
    <div class="arrows" style="position:absolute;right:0;top:6px">
      <span><svg width="10" height="12" viewBox="0 0 10 12"><path d="M8 1 2 6l6 5" fill="none" stroke="#222" stroke-width="2"/></svg></span>
      <span><svg width="10" height="12" viewBox="0 0 10 12"><path d="M2 1l6 5-6 5" fill="none" stroke="#222" stroke-width="2"/></svg></span>
    </div>
  </div>
  <div class="tiles">
    <div class="t1" role="img" aria-label="Blue printed shopping bags"></div>
    <div class="t2" role="img" aria-label="Gift boxes on a dark table"><span></span><span></span></div>
    <div class="t3" role="img" aria-label="Rolls of festive wrapping paper"></div>
    <div class="t4" role="img" aria-label="Blue tissue box with tissues"></div>
  </div>
</section>

<section class="featured">
  <div class="wrap">
    <h2 class="section-title">Featured <span class="accent">Products</span></h2>
    <div class="feat-row">
      <article class="feat"><div class="img" role="img" aria-label="Tissue box on a desk" style="background:linear-gradient(135deg,#e8e8e8,#9a9a9a)"></div>
        <div class="body"><h3>Gift Boxes</h3><p>Lorem Ipsum is simply dummy text of the printing and typesetting industry.</p>
        <div class="buy"><b><small>£</small>6</b><span class="btn">Buy Now</span><span class="btn">Add to Cart</span></div></div></article>
      <article class="feat"><div class="img" role="img" aria-label="Wrapped gifts on green background" style="background:linear-gradient(135deg,#4f7a2a,#9fbf5a)"></div>
        <div class="body"><h3>Tissue paper</h3><p>Lorem Ipsum is simply dummy text of the printing and typesetting industry.</p>
        <div class="buy"><b><small>£</small>5</b><span class="btn">Buy Now</span><span class="btn">Add to Cart</span></div></div></article>
      <article class="feat"><div class="img" role="img" aria-label="Colourful wrapped sweets" style="background:linear-gradient(135deg,#a3262a,#3a4a8a 60%,#c9a23a)"></div>
        <div class="body"><h3>Wrapping Paper</h3><p>Lorem Ipsum is simply dummy text of the printing and typesetting industry.</p>
        <div class="buy"><b><small>£</small>4</b><span class="btn">Buy Now</span><span class="btn">Add to Cart</span></div></div></article>
    </div>
  </div>
</section>

<section class="newsletter">
  <div class="wrap">
    <h2>Newsletter</h2>
    <div class="field">Email</div>
    <div class="go">SUBMIT</div>
  </div>
</section>

<section class="blog">
  <div class="wrap">
    <h2 class="section-title">Our <span class="accent">Blog</span></h2>
    <div class="posts">
      <article class="post"><div class="img" role="img" aria-label="Charts and papers on a desk" style="background:linear-gradient(135deg,#cfd6de,#5d7a9a)"></div>
        <div class="body"><time><i></i>15 January 2019</time><h3>Lorem Ipsum is simply dummy text.</h3><p>Lorem Ipsum is simply dummy text of the printing and typesetting industry.</p><span class="btn">Read More</span></div></article>
      <article class="post"><div class="img" role="img" aria-label="Green workspace with office items" style="background:linear-gradient(135deg,#3f6b24,#7dbb45)"></div>
        <div class="body"><time><i></i>15 January 2019</time><h3>Lorem Ipsum is simply dummy text.</h3><p>Lorem Ipsum is simply dummy text of the printing and typesetting industry.</p><span class="btn">Read More</span></div></article>
      <article class="post"><div class="img" role="img" aria-label="Team meeting around a laptop" style="background:linear-gradient(135deg,#6b6b6b,#2c2c2c)"></div>
        <div class="body"><time><i></i>15 January 2019</time><h3>Lorem Ipsum is simply dummy text.</h3><p>Lorem Ipsum is simply dummy text of the printing and typesetting industry.</p><span class="btn">Read More</span></div></article>
    </div>
  </div>
</section>

<section class="info">
  <div class="wrap">
    <div class="about">
      <h2 class="section-title">About <span class="accent">us</span></h2>
      <h4>Lorem Ipsum is simply dummy text of the printing.</h4>
      <p>Lorem Ipsum is simply dummy text of the printing and typesetting industry. Lorem Ipsum has been the industry's standard dummy text ever since the 1500s, when an unknown printer took a galley of type and scrambled it to make a type specimen book.</p>
      <p>It has survived not only five centuries, but also the leap into electronic typesetting, remaining essentially unchanged.</p>
      <span class="more">READ MORE....</span>
    </div>
    <div class="contact">
      <h2 class="section-title">Contact <span class="accent">us</span></h2>
      <p class="lead">Lorem Ipsum is simply dummy text of the printing and typesetting.</p>
      <div class="form">
        <div class="half">Name</div><div class="half">Phone</div>
        <div class="full">Email</div>
        <div class="full msg">Message</div>
        <span class="btn">Submit</span>
      </div>
    </div>
  </div>
</section>

<footer>
  <div class="footer">
    <div class="wrap">
      <div class="col"><h5>SITEMAP</h5><ul><li class="b">Home</li><li class="b">Products</li><li class="b">Gallery</li><li class="b">About us</li><li class="b">Contact us</li></ul></div>
      <div class="col"><h5>OUR POLICY</h5><ul><li class="b">Privacy Policy</li><li class="b">Terms Of Use</li><li class="b">Terms Of Sale</li><li class="b">FAQ</li><li class="b">Return Policy</li></ul></div>
      <div class="col"><h5>OUR INFO</h5><ul><li><span class="ico"></span>+1-555-014-2291</li><li><span class="ico"></span>213-820 Lorem Ipsum Simply<br>dummy text</li><li><span class="ico"></span>info@harbourlinebag.com</li></ul></div>
      <div class="col"><h5>GET IN TOUCH</h5><ul><li><span class="ico"></span>Friendwall</li><li><span class="ico"></span>Workline</li><li><span class="ico"></span>Chirper</li><li><span class="ico"></span>Circleplus</li></ul></div>
    </div>
  </div>
  <div class="copy">©2019 <b>Harbourline Bag</b>. All Right Reserved. | Terms &amp; Conditions.</div>
</footer>

</body>
</html>
```